Flyer-Design für Rasseclub
sehr angenehme Zusammenarbeit - tolle Vorschläge - Anregungen werden prompt umgesetzt. Vielen Dank für den schönen Flyer. Vom Drucker habe ich auch noch ein Lob erhalten. "Nicht jeder Grafiker / Designer liefere solche gute Qualität ab"
Zielgruppe
Wir sind ein Rasseclub für die Zebu-Züchter in der Schweiz. Wir setzen uns für die Interessen und die Verbreitung der Zeburinder ein. Mit unserem Flyer versuchen wir interessierten Personen einen kurzen Überblick über die Rasse zu verschaffen.
Aufgabenstellung
Wir wünschen uns einen Flyer im A4 Format, welcher 1 oder 2x gefalzt ist. Vorne und hinten Beschriftet / Gestaltet.

```html
<!DOCTYPE html>
<html lang="de">
<head>
<meta charset="utf-8">
<title>Rasseclub Höckerrind Schweiz – Flyer</title>
<link href="https://fonts.googleapis.com/css2?family=Open+Sans:wght@300;400;700&display=swap" rel="stylesheet">
<style>
  :root{
    --olive:#626a37;
    --olive-light:#868a63;
    --red:#e31e24;
    --white:#ffffff;
    --ink:#2a2a2a;
    --stage:#e2e2e2;
    --grass-top:#9cae6a;
    --grass-bottom:#6d8a3c;
  }
  *{margin:0;padding:0;box-sizing:border-box}
  html,body{width:1200px;height:3905px;overflow:hidden;background:var(--stage)}
  body{position:relative;font-family:"Open Sans",Arial,sans-serif;color:var(--ink)}

  .sheet{position:absolute;display:flex;box-shadow:0 3px 8px rgba(0,0,0,.28)}
  .panel{position:relative;width:319px;height:678px;background:var(--white);overflow:hidden}
  .panel--olive{background:var(--olive);color:var(--white)}
  .panel::after{content:"";position:absolute;left:0;right:0;bottom:0;height:15px;background:var(--red)}

  .photo{position:absolute;left:0;right:0}
  .photo--grass{background:linear-gradient(180deg,var(--grass-top),var(--grass-bottom))}
  .photo--cow{background:linear-gradient(180deg,#9fb36d 0%,#7d8f4c 45%,#6a4a3a 50%,#7d8f4c 70%,#c9b79a 100%)}
  .photo--herd{background:linear-gradient(180deg,#b9c3c4 0%,#9bae70 35%,#c9c5bd 55%,#6d8a3c 100%)}
  .photo--closeup{background:linear-gradient(180deg,#c5d2de 0%,#e9dccb 40%,#d9c4ad 70%,#a7b06e 100%)}
  .photo--field{background:linear-gradient(180deg,#c9cfd1 0%,#97a38b 35%,#7f9a48 60%,#a86c48 72%,#6d8a3c 100%)}
  .strip{position:absolute;left:0;right:0;height:16px;background:var(--olive-light)}

  .brand{position:absolute;left:0;right:0;text-align:center;font-weight:700;font-size:22px;letter-spacing:2px}
  .brand span{display:inline-block;width:12px;height:12px;background:var(--red);margin-right:8px;vertical-align:middle}
  .brand--dark{color:var(--ink)}
  .brand--light{color:var(--white)}
  .logo-area{position:absolute;left:0;right:0;top:0;height:118px;background:var(--white)}

  .title-block{position:absolute;right:26px;text-align:right;color:var(--white)}
  .title-block .kicker{font-weight:300;font-size:20px;line-height:1.2}
  .title-block .name{font-weight:700;font-size:24px;letter-spacing:.5px;line-height:1.3}

  .copy{position:absolute;left:34px;right:30px}
  .copy h2{font-size:15px;font-weight:700;text-transform:uppercase;letter-spacing:.3px;padding-bottom:12px}
  .copy h2::after{content:"";display:block;width:234px;height:2px;background:var(--red);margin-top:12px}
  .copy p{font-size:11.2px;line-height:1.35;margin-bottom:7px}

  .contact{position:absolute;left:32px;width:251px;height:170px;background:var(--white);border-bottom:15px solid var(--olive-light);color:#555;font-size:10.5px;padding:12px 13px}
</style>
</head>
<body>

<!-- Front cover -->
<section class="sheet" style="left:438px;top:88px">
  <article class="panel panel--olive">
    <div class="logo-area"><div class="brand brand--dark" style="top:44px"><span></span>HÖCKERRIND</div></div>
    <div class="photo photo--cow" style="top:118px;height:392px" role="img" aria-label="Foto: braunes Zeburind auf einer Weide"></div>
    <div class="strip" style="top:510px"></div>
    <div class="title-block" style="top:560px"><div class="kicker">Rasseclub</div><div class="name">HÖCKERRIND SCHWEIZ</div></div>
  </article>
</section>

<!-- Outside spread -->
<section class="sheet" style="left:120px;top:845px">
  <article class="panel">
    <div class="photo photo--herd" style="top:0;height:353px" role="img" aria-label="Foto: gefleckte und graue Zebus auf der Weide"></div>
    <div class="copy" style="top:395px">
      <h2>Herkunft</h2>
      <p>Die Zebus (Bos indicus) gehören zu den Buckelrindern, die sich nicht nur vom Erbgut, sondern auch vom äusseren Erscheinungsbild her stark von den anderen Rinderrassen in Europa unterscheiden. Die Zebus stammen ursprünglich aus Sri Lanka und dem südlichen Kaukasus. Heute sind sie auf der ganzen Welt verbreitet. Die Zeburasse wird in 600 Rasseschläge unterteilt: vom kleinsten Zwergzebu bis zu den grössten Brahma oder Nelore. Das Wort Zebu wird vom tibetanischen Wort „zeu“ respektive. „zeba“ abgeleitet, welches übersetzt Buckel heisst.</p>
    </div>
  </article>
  <article class="panel panel--olive">
    <div class="brand brand--light" style="top:60px"><span></span>HÖCKERRIND</div>
    <div class="copy" style="top:165px">
      <h2>Rasseclub</h2>
      <p>Bei «Weidekuh Verband» sind über 150 Muttertiere der Rasse Zwergzebu und Zebu registriert. Der «Rasseclub Höckerrind Schweiz» gibt es seit dem Jahr 2015. Alle, die Zebus in der Schweiz halten, sind im Rasseclub herzlich willkommen. Die Tiere können, wie jedes andere Rind auch, bei «Weidekuh Verband» angemeldet werden. Selbstverständlich können auch die anerkannten Stiere im Herdebuch von «Weidekuh Verband» aufgenommen werden und sind somit als Zuchtstiere anerkannt.</p>
    </div>
    <div class="contact" style="top:447px">Ihr Zebuhalter in der Nähe:</div>
  </article>
  <article class="panel panel--olive">
    <div class="logo-area"><div class="brand brand--dark" style="top:44px"><span></span>HÖCKERRIND</div></div>
    <div class="photo photo--cow" style="top:118px;height:392px" role="img" aria-label="Foto: braunes Zeburind auf einer Weide"></div>
    <div class="strip" style="top:510px"></div>
    <div class="title-block" style="top:560px"><div class="kicker">Rasseclub</div><div class="name">HÖCKERRIND SCHWEIZ</div></div>
  </article>
</section>

<!-- Inside spread -->
<section class="sheet" style="left:120px;top:1588px">
  <article class="panel">
    <div class="photo photo--grass" style="top:0;height:260px" role="img" aria-label="Foto: weiss-braun geflecktes Zebu im Gras"></div>
    <div class="strip" style="top:260px"></div>
    <div class="copy" style="top:325px">
      <h2>Merkmale und Eigenschaften</h2>
      <p>Der Buckel ist das auffälligste, äussere Merkmal der Zeburinder. Das ausgesprochen marmorierte Buckelfleisch ist eine Delikatesse. Das übrige Muskelfleisch ist sehr fettarm, mit einem leichten Wildgeschmack, feinfaserig und enthält die gesunden Omega-3-Fettsäuren.</p>
      <p>Zum typischen Erscheinungsbild der Zebus gehören neben dem Buckel die Hörner, eine starke Wamme, ein abgezogenes und stark abgedachtes Becken, feine Extremitäten und eine schmale Stirn, die dem Kopf eine längliche Form verleiht.</p>
      <p>Die Grösse der Tiere kann stark variieren. Die Kühe sind deutlich kleiner als die Stiere. Zebus kommen in allen Farben und Farbkombinationen vor. Auch die Hörner sind nicht immer klassisch nach oben gerichtet.</p>
    </div>
  </article>
  <article class="panel">
    <div class="copy" style="top:53px"><p>Zebus sind sehr robust und gehören zu den extensiven Rinderrassen. Die Klauenpflege kann auf ein Minimum beschränkt werden. Die Tiere sind betreffend Futter sehr genügsam. Ihnen reicht im Sommer Gras und im Winter Heu. Auf Kraftfutter und andere Zusätze, mit Ausnahme von Salz, kann verzichtet werden. Die Abkalbung ist meist leicht und geschieht ohne menschliche Hilfe. Die Mutterkühe haben einen guten Schutzinstinkt für ihre Kälber.</p></div>
    <div class="photo photo--closeup" style="top:223px;height:212px" role="img" aria-label="Foto: helles Zebu in Nahaufnahme vor Landschaft"></div>
    <div class="strip" style="top:435px"></div>
    <div class="copy" style="top:497px"><p>Während die meisten europäischen Rinderrassen unter der Sommerhitze leiden, fühlen sich Zebus bei Temperaturen um 30 Grad noch wohl. Ihr schütteres Fell und die dicke Aussenhaut schützen sie vor der Hitze. In den letzten Jahren wurde beobachtet, dass Zebusperma auch bei Temperaturen über 38°C noch befruchtungsfähig bleibt. Kalte Temperaturen sind sie sich von ihrer Heimat auch gewohnt.</p></div>
  </article>
  <article class="panel">
    <div class="photo photo--grass" style="top:0;height:232px" role="img" aria-label="Foto: weisses Zebukalb auf der Wiese"></div>
    <div class="strip" style="top:232px"></div>
    <div class="copy" style="top:300px">
      <h2>Einsatz</h2>
      <p>Durch ihr leichtes Gewicht verursachen Zebus kaum Trittschäden, wodurch sie fast überall einsetzbar sind. Sie können auch gut zur allgemeinen Landschaftspflege eingesetzt werden.</p>
    </div>
    <div class="photo photo--field" style="top:455px;height:208px" role="img" aria-label="Foto: Herde brauner Zebus im Nebel auf der Weide"></div>
  </article>
</section>

<!-- Folded view, shown flat -->
<section class="sheet" style="left:281px;top:2360px">
  <article class="panel">
    <div class="photo photo--grass" style="top:0;height:260px" role="img" aria-label="Foto: weiss-braun geflecktes Zebu im Gras"></div>
    <div class="strip" style="top:260px"></div>
    <div class="copy" style="top:325px">
      <h2>Merkmale und Eigenschaften</h2>
      <p>Der Buckel ist das auffälligste, äussere Merkmal der Zeburinder. Das ausgesprochen marmorierte Buckelfleisch ist eine Delikatesse. Das übrige Muskelfleisch ist sehr fettarm, mit einem leichten Wildgeschmack, feinfaserig und enthält die gesunden Omega-3-Fettsäuren.</p>
      <p>Zum typischen Erscheinungsbild der Zebus gehören neben dem Buckel die Hörner, eine starke Wamme, ein abgezogenes und stark abgedachtes Becken, feine Extremitäten und eine schmale Stirn, die dem Kopf eine längliche Form verleiht.</p>
      <p>Die Grösse der Tiere kann stark variieren. Die Kühe sind deutlich kleiner als die Stiere. Zebus kommen in allen Farben und Farbkombinationen vor. Auch die Hörner sind nicht immer klassisch nach oben gerichtet.</p>
    </div>
  </article>
  <article class="panel">
    <div class="photo photo--herd" style="top:0;height:353px" role="img" aria-label="Foto: gefleckte und graue Zebus auf der Weide"></div>
    <div class="copy" style="top:395px">
      <h2>Herkunft</h2>
      <p>Die Zebus (Bos indicus) gehören zu den Buckelrindern, die sich nicht nur vom Erbgut, sondern auch vom äusseren Erscheinungsbild her stark von den anderen Rinderrassen in Europa unterscheiden. Die Zebus stammen ursprünglich aus Sri Lanka und dem südlichen Kaukasus. Heute sind sie auf der ganzen Welt verbreitet. Die Zeburasse wird in 600 Rasseschläge unterteilt: vom kleinsten Zwergzebu bis zu den grössten Brahma oder Nelore. Das Wort Zebu wird vom tibetanischen Wort „zeu“ respektive. „zeba“ abgeleitet, welches übersetzt Buckel heisst.</p>
    </div>
  </article>
</section>

<!-- Back panel -->
<section class="sheet" style="left:438px;top:3114px">
  <article class="panel panel--olive">
    <div class="brand brand--light" style="top:60px"><span></span>HÖCKERRIND</div>
    <div class="copy" style="top:165px">
      <h2>Rasseclub</h2>
      <p>Bei «Weidekuh Verband» sind über 150 Muttertiere der Rasse Zwergzebu und Zebu registriert. Der «Rasseclub Höckerrind Schweiz» gibt es seit dem Jahr 2015. Alle, die Zebus in der Schweiz halten, sind im Rasseclub herzlich willkommen. Die Tiere können, wie jedes andere Rind auch, bei «Weidekuh Verband» angemeldet werden. Selbstverständlich können auch die anerkannten Stiere im Herdebuch von «Weidekuh Verband» aufgenommen werden und sind somit als Zuchtstiere anerkannt.</p>
    </div>
    <div class="contact" style="top:447px">Ihr Zebuhalter in der Nähe:</div>
  </article>
</section>

</body>
</html>
```